BEACON CABS

Taxi card design

Need changes very slow in replying to my messages.

Target Market(s)

Customers

Industry/Entity Type

Taxi

Contact Information for Business Card

See previous design

Font styles to use
Sans Serif

Colors
A7469A
B969AE
D3A5CF
EDDBEB
F8F0F9
6B429C
8869AF
B7A5CE
E3DAEB
F3F0F8

Requirements
Nice to have
• We are in the business of looking after people, not just driving vehicles front
Should not have
• Front number 01632 480 480 needs to big big

```html
<!DOCTYPE html>
<html lang="en">
<head>
<meta charset="utf-8">
<title>Beacon Cabs – Business Card</title>
<link href="https://fonts.googleapis.com/css2?family=Arimo:wght@400;700&family=Michroma&display=swap" rel="stylesheet">
<style>
  :root {
    --stage: #2a2a2c;
    --card: #121212;
    --white: #ffffff;
    --grey: #b9b9b9;
    --violet: #6b429c;
    --magenta: #a7469a;
    --orchid: #b969ae;
  }
  * { box-sizing: border-box; margin: 0; padding: 0; }
  html, body { width: 1200px; height: 900px; overflow: hidden; }
  body {
    background: var(--stage);
    font-family: "Arimo", Arial, sans-serif;
    color: var(--white);
    position: relative;
  }
  .card {
    position: absolute;
    left: 320px;
    width: 560px;
    height: 320px;
    background: var(--card);
    overflow: hidden;
    box-shadow: 0 10px 30px rgba(0,0,0,.5);
  }
  .card--front { top: 110px; }
  .card--back { top: 470px; }

  .brand {
    position: absolute;
    font-family: "Arimo", Arial, sans-serif;
    font-weight: 700;
    color: var(--white);
    letter-spacing: 1px;
    white-space: nowrap;
    display: flex;
    align-items: center;
    gap: 14px;
  }
  .brand__mark {
    width: 22px; height: 22px;
    background: var(--magenta);
    flex: none;
  }
  .card--front .brand { left: 130px; top: 92px; font-size: 48px; }
  .tagline {
    position: absolute;
    right: 60px; top: 168px;
    font-size: 14px;
    color: var(--grey);
  }
  .band {
    position: absolute;
    left: 0; right: 0; bottom: 0;
    background: linear-gradient(90deg, var(--violet), var(--magenta));
    display: flex;
    align-items: center;
  }
  .card--front .band {
    height: 58px;
    justify-content: center;
    gap: 12px;
    font-size: 17px;
  }
  .band__dot {
    width: 9px; height: 9px; border-radius: 50%;
    background: var(--white);
  }

  .card--back .brand { left: 160px; top: 42px; font-size: 40px; }
  .contact {
    position: absolute;
    display: flex;
    align-items: center;
    gap: 8px;
    font-size: 13.5px;
    white-space: nowrap;
  }
  .contact__icon {
    width: 18px; height: 16px;
    background: var(--magenta);
    border-radius: 3px;
    display: flex; align-items: center; justify-content: center;
    flex: none;
  }
  .contact__icon svg { width: 11px; height: 11px; }
  .contact__label { color: var(--orchid); }
  .address {
    position: absolute;
    left: 318px; top: 190px;
    font-size: 13.5px;
    line-height: 16px;
    display: flex;
    gap: 8px;
  }
  .card--back .band {
    height: 66px;
    padding-left: 32px;
    gap: 18px;
  }
  .hotline__icon {
    width: 34px; height: 32px;
    background: var(--white);
    border-radius: 4px;
    display: flex; align-items: center; justify-content: center;
  }
  .hotline__icon svg { width: 22px; height: 22px; }
  .hotline__number {
    font-family: "Michroma", "Arimo", sans-serif;
    font-size: 30px;
    letter-spacing: 2px;
    color: var(--white);
  }
</style>
</head>
<body>

<section class="card card--front">
  <div class="brand"><span class="brand__mark"></span>BEACON CABS</div>
  <p class="tagline">24/7 service</p>
  <div class="band">
    <span>Airport Transfers</span><span class="band__dot"></span>
    <span>Minibuses</span><span class="band__dot"></span>
    <span>School Transport</span>
  </div>
</section>

<section class="card card--back">
  <div class="brand"><span class="brand__mark"></span>BEACON CABS</div>

  <div class="contact" style="left:40px; top:128px;">
    <span class="contact__icon"><svg viewBox="0 0 24 24"><path fill="#fff" d="M6.6 10.8a15.1 15.1 0 0 0 6.6 6.6l2.2-2.2c.3-.3.7-.4 1-.2 1.1.4 2.3.6 3.6.6.6 0 1 .4 1 1V20c0 .6-.4 1-1 1A17 17 0 0 1 3 4c0-.6.4-1 1-1h3.5c.6 0 1 .4 1 1 0 1.3.2 2.5.6 3.6.1.3 0 .7-.2 1z"/></svg></span>
    01632 960 166
  </div>
  <div class="contact" style="left:212px; top:128px;">
    <span class="contact__icon"><svg viewBox="0 0 24 24"><path fill="#fff" d="M6.6 10.8a15.1 15.1 0 0 0 6.6 6.6l2.2-2.2c.3-.3.7-.4 1-.2 1.1.4 2.3.6 3.6.6.6 0 1 .4 1 1V20c0 .6-.4 1-1 1A17 17 0 0 1 3 4c0-.6.4-1 1-1h3.5c.6 0 1 .4 1 1 0 1.3.2 2.5.6 3.6.1.3 0 .7-.2 1z"/></svg></span>
    01632 960 020
  </div>
  <div class="contact" style="left:384px; top:128px;">
    <span class="contact__icon"><svg viewBox="0 0 24 24"><path fill="#fff" d="M6.6 10.8a15.1 15.1 0 0 0 6.6 6.6l2.2-2.2c.3-.3.7-.4 1-.2 1.1.4 2.3.6 3.6.6.6 0 1 .4 1 1V20c0 .6-.4 1-1 1A17 17 0 0 1 3 4c0-.6.4-1 1-1h3.5c.6 0 1 .4 1 1 0 1.3.2 2.5.6 3.6.1.3 0 .7-.2 1z"/></svg></span>
    01632 960 811
  </div>

  <div class="contact" style="left:40px; top:170px;">
    <span class="contact__icon"><svg viewBox="0 0 24 24"><path fill="#fff" d="M6.6 10.8a15.1 15.1 0 0 0 6.6 6.6l2.2-2.2c.3-.3.7-.4 1-.2 1.1.4 2.3.6 3.6.6.6 0 1 .4 1 1V20c0 .6-.4 1-1 1A17 17 0 0 1 3 4c0-.6.4-1 1-1h3.5c.6 0 1 .4 1 1 0 1.3.2 2.5.6 3.6.1.3 0 .7-.2 1z"/></svg></span>
    <span><span class="contact__label">Freephone:</span> 0808 157 0 222</span>
  </div>
  <div class="contact" style="left:40px; top:192px;">
    <span class="contact__icon"><svg viewBox="0 0 24 24"><rect x="3" y="6" width="18" height="12" fill="none" stroke="#fff" stroke-width="2"/><path d="M3 6l9 7 9-7" fill="none" stroke="#fff" stroke-width="2"/></svg></span>
    bookings@beaconcabs.co.uk
  </div>
  <div class="contact" style="left:40px; top:214px;">
    <span class="contact__icon"><svg viewBox="0 0 24 24"><circle cx="12" cy="12" r="9" fill="none" stroke="#fff" stroke-width="2"/><path d="M3 12h18M12 3c3 3 3 15 0 18M12 3c-3 3-3 15 0 18" fill="none" stroke="#fff" stroke-width="1.6"/></svg></span>
    www.beaconcabs.co.uk
  </div>

  <div class="address">
    <span class="contact__icon"><svg viewBox="0 0 24 24"><path fill="#fff" d="M12 2a7 7 0 0 0-7 7c0 5 7 13 7 13s7-8 7-13a7 7 0 0 0-7-7zm0 9.5A2.5 2.5 0 1 1 12 6.5a2.5 2.5 0 0 1 0 5z"/></svg></span>
    <span>St Marks Church Hall,<br>Market Row Northby<br>NB14 3QT</span>
  </div>

  <div class="band">
    <span class="hotline__icon"><svg viewBox="0 0 24 24"><path fill="#8869af" d="M6.6 10.8a15.1 15.1 0 0 0 6.6 6.6l2.2-2.2c.3-.3.7-.4 1-.2 1.1.4 2.3.6 3.6.6.6 0 1 .4 1 1V20c0 .6-.4 1-1 1A17 17 0 0 1 3 4c0-.6.4-1 1-1h3.5c.6 0 1 .4 1 1 0 1.3.2 2.5.6 3.6.1.3 0 .7-.2 1z"/></svg></span>
    <span class="hotline__number">01632 480 480</span>
  </div>
</section>

</body>
</html>
```